Boom Way Hoist Service Business Cards

I need a business card for "Boom Way Hoist and Haulage"

Boomway2023@hoistmail.net

Hoist Works LLC, Boom Way Hoist and Haulage LLC

555.014.7260 | www.BOOMWAYHOISTS.example

Central Westplain & Northeast Lakeland

(WP) 14820 Maple Lane Fairbrook, WP 46000

(LK) 2450 Pell Street Oakridge, Lakeland 44300

Colors
0094D4
00A9DD
6FCCEA
C7EBF8
E9F6FB
59FF00
82FF00
B8FF75
E3FFCB
F4FFEA
EE7325
F08F49
F5BC92
FAE3D3
FDF4ED
EB3D1F
EC4F4E
F09395
F8D3D4
FCEDEE
E54698
E96AAD
F1A4CE
F9D9EA
FCEFF6
A7469A
B969AE
D3A5CF
EDDBEB
F8F0F9

```html
<!DOCTYPE html>
<html lang="en">
<head>
<meta charset="utf-8">
<title>Boom Way Hoist and Haulage — Business Cards</title>
<link href="https://fonts.googleapis.com/css2?family=Montserrat:wght@500;600;700;800&display=swap" rel="stylesheet">
<style>
  :root {
    --backdrop: #3b3b3b;
    --card-black: #121212;
    --card-white: #ffffff;
    --brand-green: #2ecc40;
    --text-light: #f2f2f2;
    --text-dark: #1a1a1a;
  }
  * { box-sizing: border-box; margin: 0; padding: 0; }
  html, body {
    width: 1200px; height: 1200px; overflow: hidden;
    background: var(--backdrop);
    font-family: "Montserrat", sans-serif;
  }
  .sheet {
    width: 1200px; height: 1200px;
    display: flex; flex-direction: column; align-items: center; justify-content: center;
    gap: 56px;
  }
  .card {
    width: 900px; height: 514px;
    border-radius: 38px;
    overflow: hidden;
    position: relative;
    box-shadow: 0 18px 40px rgba(0,0,0,.45);
  }
  .card-front { display: flex; background: var(--card-white); }
  .contact-panel {
    width: 470px; background: var(--card-black);
    padding: 120px 0 0 70px;
    color: var(--text-light);
  }
  .divider { width: 14px; background: var(--brand-green); }
  .divider-gap { width: 12px; background: var(--card-white); }
  .company-names {
    color: var(--brand-green);
    font-weight: 700; font-size: 17px; line-height: 1.2;
    text-transform: uppercase; letter-spacing: .3px;
    margin-bottom: 26px;
  }
  .contact-list { list-style: none; margin-bottom: 22px; }
  .contact-list li {
    display: flex; align-items: center; gap: 12px;
    font-size: 16px; font-weight: 500; line-height: 1.75;
  }
  .contact-list svg { width: 18px; height: 18px; flex: none; }
  .region {
    color: var(--brand-green); font-weight: 600; font-size: 16px;
    margin-bottom: 6px;
  }
  .address { font-size: 15px; font-weight: 500; line-height: 1.55; }
  .brand-panel {
    flex: 1; display: flex; align-items: center; justify-content: center;
    gap: 14px;
  }
  .brand-mark { width: 18px; height: 18px; background: var(--brand-green); flex: none; }
  .brand-name {
    font-weight: 800; font-size: 40px; line-height: 1.05;
    color: var(--text-dark); text-transform: uppercase;
  }
  .card-back {
    background: var(--card-black);
    display: flex; align-items: center; justify-content: center; gap: 18px;
  }
  .card-back .brand-name { color: var(--card-white); font-size: 52px; }
</style>
</head>
<body>
<main class="sheet">
  <section class="card card-front" aria-label="Card front">
    <div class="contact-panel">
      <p class="company-names">Hoist Works LLC,<br>Boom Way Hoist and Haulage LLC</p>
      <ul class="contact-list">
        <li>
          <svg viewBox="0 0 24 24" aria-hidden="true"><path fill="#2ecc40" d="M6.6 10.8a15.1 15.1 0 0 0 6.6 6.6l2.2-2.2c.3-.3.7-.4 1-.2 1.1.4 2.3.6 3.6.6.6 0 1 .4 1 1V20c0 .6-.4 1-1 1A17 17 0 0 1 3 4c0-.6.4-1 1-1h3.5c.6 0 1 .4 1 1 0 1.3.2 2.5.6 3.6.1.3 0 .7-.2 1z"/></svg>
          555.014.7260
        </li>
        <li>
          <svg viewBox="0 0 24 24" aria-hidden="true"><rect x="2" y="5" width="20" height="14" rx="1.5" fill="#2ecc40"/><path d="M2.5 6l9.5 7 9.5-7" fill="none" stroke="#121212" stroke-width="1.8"/></svg>
          Boomway2023@hoistmail.net
        </li>
        <li>
          <svg viewBox="0 0 24 24" aria-hidden="true" fill="none" stroke="#2ecc40" stroke-width="1.8"><circle cx="12" cy="12" r="9.5"/><ellipse cx="12" cy="12" rx="4.2" ry="9.5"/><path d="M2.5 12h19M4 7h16M4 17h16"/></svg>
          www.BOOMWAYHOISTS.example
        </li>
      </ul>
      <p class="region">Central Westplain &amp; Northeast Lakeland</p>
      <p class="address">(WP) 14820 Maple Lane Fairbrook, WP 46000<br>(LK) 2450 Pell Street Oakridge, Lakeland 44300</p>
    </div>
    <div class="divider-gap"></div>
    <div class="divider"></div>
    <div class="brand-panel">
      <span class="brand-mark" aria-hidden="true"></span>
      <p class="brand-name">Boom Way<br>Hoist and<br>Haulage</p>
    </div>
  </section>

  <section class="card card-back" aria-label="Card back">
    <span class="brand-mark" aria-hidden="true"></span>
    <p class="brand-name">Boom Way<br>Hoist and Haulage</p>
  </section>
</main>
</body>
</html>
```